Up to the Challenge? Canadian based consulting company needs a two sided business card design

A Canadian based security risk management consulting company needs a two-sided business card design. What we do is provide advice and guidance related to emergency, security and business continuity management for small, medium and large companies to help ensure the protection of their people, assets, information, services, operations and reputation.

The final design should be simple, only one or two colours, eye catching, professional and one that makes people look at three or more times just because it looks so darn good.

I have include examples of business cards I like.

Target Market(s)

Small, medium and large companies.

Industry/Entity Type

Security

Contact Information for Business Card

Business Card Size: Standard size of 3.5" (89mm) x 2.0" (51mm) - (see full specifications and guides on PRINTA's website if required)
Card Stock: Looking to use PRINTA's Velda 32pt stock textured paper - seam colour either chili red or black
Business Name: The Harrowfield Group
Website: www.theharrowfieldgroup.example
Telephone: (555)214-0397
Name: Dana Forsythe
Position: Principle
e-mail: Dana.Forsythe@theharrowfieldgroup.example

Font styles to use
Serif

Colors
ec1f27
000000
9d9d9d
aaaaaa
606060

Requirements
Must have
• - "The Harrowfield Group" logo (see uploaded files). I have included grey scale and colour versions.
• - Business card details (as above)
Nice to have
• - One side black or grey scale.
• - Other side would likely be white.
• - Everyone likes the silver logo on the black background.
• - Small element of colour i.e. red but I'm leaning more to greyscale.
Should not have
• - A lot of colour. Keep it simple.

```html
<!DOCTYPE html>
<html lang="en">
<head>
<meta charset="utf-8">
<title>The Harrowfield Group – Business Card</title>
<link href="https://fonts.googleapis.com/css2?family=Comfortaa:wght@400&family=Open+Sans:wght@400;600&display=swap" rel="stylesheet">
<style>
  :root {
    --brand-red: #ec1f27;
    --ink: #1a1a1a;
    --band: #5c5c5c;
    --card: #ffffff;
    --card-dark-top: #3c3c3e;
    --card-dark-bottom: #262628;
    --backdrop: #d6d6d6;
    --white: #ffffff;
  }
  * { margin: 0; padding: 0; box-sizing: border-box; }
  html, body {
    width: 1200px; height: 676px; overflow: hidden;
    background: var(--backdrop);
  }
  .stage { position: relative; width: 1200px; height: 676px; }

  .card {
    position: absolute; top: 178px;
    width: 560px; height: 320px;
    box-shadow: 0 6px 18px rgba(0,0,0,0.18);
    overflow: hidden;
  }

  /* Back side */
  .card-back {
    left: 20px;
    background: linear-gradient(160deg, var(--card-dark-top), var(--card-dark-bottom));
    display: flex; flex-direction: column; align-items: center; justify-content: center; gap: 14px;
  }
  .card-back .mark-square { width: 56px; height: 56px; background: var(--brand-red); }
  .card-back .mark-name {
    font-family: "Open Sans", sans-serif; font-weight: 600;
    font-size: 22px; letter-spacing: 1px; color: var(--brand-red);
    text-transform: uppercase; text-align: center; line-height: 1.25;
  }

  /* Front side */
  .card-front { left: 620px; background: var(--card); }
  .holder {
    position: absolute; right: 100px; top: 40px;
    text-align: right;
    font-family: "Comfortaa", sans-serif;
    color: var(--ink);
  }
  .holder-name { font-size: 40px; line-height: 1.1; letter-spacing: 0.3px; white-space: nowrap; }
  .holder-title { font-size: 29px; line-height: 1.15; margin-right: -27px; }
  .company-mark {
    position: absolute; left: 34px; top: 104px;
    display: flex; flex-direction: column; align-items: center; gap: 5px;
  }
  .company-mark .mark-square { width: 22px; height: 22px; background: var(--brand-red); }
  .company-mark .mark-name {
    font-family: "Open Sans", sans-serif; font-weight: 600;
    font-size: 10px; letter-spacing: 0.4px; color: var(--brand-red);
    text-transform: uppercase; text-align: center; line-height: 1.2;
  }
  .phone-band {
    position: absolute; left: 0; top: 164px; width: 100%; height: 72px;
    background: var(--band);
    display: flex; align-items: center; justify-content: center; gap: 10px;
    color: var(--white);
    font-family: "Open Sans", sans-serif; font-weight: 600; font-size: 31px;
  }
  .phone-band svg { width: 26px; height: 26px; }
  .contact-list {
    position: absolute; left: 30px; top: 250px;
    list-style: none;
    font-family: "Open Sans", sans-serif; font-size: 11.5px; color: var(--ink);
  }
  .contact-list li { display: flex; align-items: center; gap: 4px; line-height: 1.45; white-space: nowrap; }
  .contact-list svg { width: 11px; height: 11px; flex: none; }
  .contact-list .plain-square { width: 10px; height: 10px; background: var(--ink); flex: none; }
</style>
</head>
<body>
<main class="stage">
  <section class="card card-back">
    <span class="mark-square"></span>
    <span class="mark-name">The Harrowfield<br>Group</span>
  </section>

  <section class="card card-front">
    <div class="holder">
      <div class="holder-name">Dana Forsythe</div>
      <div class="holder-title">Principle</div>
    </div>

    <div class="company-mark">
      <span class="mark-square"></span>
      <span class="mark-name">The Harrowfield<br>Group</span>
    </div>

    <div class="phone-band">
      <svg viewBox="0 0 24 24" aria-hidden="true"><path fill="#fff" d="M6.6 10.8a15.1 15.1 0 0 0 6.6 6.6l2.2-2.2a1 1 0 0 1 1-.25 11.4 11.4 0 0 0 3.6.57 1 1 0 0 1 1 1V20a1 1 0 0 1-1 1A17 17 0 0 1 3 4a1 1 0 0 1 1-1h3.5a1 1 0 0 1 1 1c0 1.25.2 2.45.57 3.57a1 1 0 0 1-.25 1z"/></svg>
      <span>: (555)214-0397</span>
    </div>

    <ul class="contact-list">
      <li>
        <svg viewBox="0 0 16 16" aria-hidden="true"><rect x="1" y="3" width="14" height="10" fill="none" stroke="#1a1a1a" stroke-width="1.4"/><path d="M1 3l7 6 7-6" fill="none" stroke="#1a1a1a" stroke-width="1.4"/></svg>
        <span>: Dana.Forsythe@theharrowfieldgroup.example</span>
      </li>
      <li>
        <svg viewBox="0 0 16 16" aria-hidden="true"><circle cx="8" cy="8" r="6.5" fill="#1a1a1a"/></svg>
        <span>: www.theharrowfieldgroup.example</span>
      </li>
      <li>
        <span class="plain-square"></span>
        <span>: https://profiles.example/in/danaforsythe</span>
      </li>
    </ul>
  </section>
</main>
</body>
</html>
```